Lumigram Page Design for a Medical Billing Business

We need help designing a lumigram page that is professional, yet friendly that will attract medical practitioners (doctors, therapists, nutritionists, chiropractors, etc) to check out and follow our business. I have attached our logo which must be incorporated in the design.

```html
<!DOCTYPE html>
<html lang="en">
<head>
<meta charset="utf-8">
<title>Vela Medical Billing – Lumigram Cover</title>
<link rel="stylesheet" href="https://fonts.googleapis.com/css2?family=Anton&family=Tinos:ital,wght@0,400;1,400;1,700&display=swap">
<style>
  :root {
    --stage: #2b3038;
    --paper: #f7f8fa;
    --sky: #1f9ad8;
    --navy: #2a2270;
    --violet: #4a2d8f;
    --plum: #8a3c9c;
    --pink-dot: #c75ba0;
    --ink: #3a3a48;
    --white: #ffffff;
  }
  * { margin: 0; padding: 0; box-sizing: border-box; }
  html, body { width: 1039px; height: 1200px; overflow: hidden; background: var(--stage); }
  .cover {
    position: absolute; left: 20px; top: 415px;
    width: 1000px; height: 370px;
    background: var(--paper); overflow: hidden;
    font-family: "Tinos", serif; color: var(--ink);
  }
  .cover-shapes { position: absolute; inset: 0; }
  .headline-script {
    position: absolute; left: 42px; top: 36px;
    font-size: 44px; color: var(--sky); line-height: 1;
  }
  .headline-bold {
    position: absolute; left: 42px; top: 82px;
    font-family: "Anton", sans-serif; font-size: 38px; line-height: 1.02;
    color: var(--navy); letter-spacing: 0.5px; text-transform: uppercase;
  }
  .service-band {
    position: absolute; left: 0; top: 169px; width: 420px; height: 29px;
    background: linear-gradient(90deg, rgba(31,154,216,0) 0%, #4aa6dc 30%, #2f6fc0 60%, rgba(47,111,192,0) 100%);
    color: var(--white); font-size: 28px; line-height: 29px; text-align: center;
    padding-left: 55px;
  }
  .service-list {
    position: absolute; top: 203px; list-style: none;
    font-size: 19px; line-height: 27px;
  }
  .service-list li::before {
    content: ""; display: inline-block; width: 9px; height: 9px;
    border-radius: 50%; background: var(--pink-dot); margin-right: 4px; vertical-align: 2px;
  }
  .service-list--left { left: 46px; }
  .service-list--right { left: 362px; }
  .contact-row {
    position: absolute; top: 317px; height: 53px; line-height: 53px;
    color: var(--white); font-size: 18px;
  }
  .contact-phone { left: 46px; font-style: italic; font-weight: 700; }
  .contact-phone svg { vertical-align: -2px; margin-right: 6px; }
  .contact-email { left: 227px; }
  .contact-web { left: 482px; }
  .brand-name {
    position: absolute; left: 820px; top: 50px;
    font-size: 24px; color: var(--violet); letter-spacing: 2px; line-height: 1.1;
    text-align: center; width: 150px;
  }
  .brand-name .brand-dot {
    display: block; width: 10px; height: 10px; border-radius: 50%;
    background: var(--violet); margin: 0 auto 6px;
  }
</style>
</head>
<body>
  <section class="cover" aria-label="Vela Medical Billing cover banner">
    <svg class="cover-shapes" width="1000" height="370" viewBox="0 0 1000 370">
      <defs>
        <linearGradient id="bar-gradient" x1="0" x2="1" y1="0" y2="0">
          <stop offset="0" stop-color="#4a2d8f"/>
          <stop offset="0.55" stop-color="#5b3296"/>
          <stop offset="1" stop-color="#8a3c9c"/>
        </linearGradient>
        <linearGradient id="desk-photo" x1="0" x2="1" y1="0" y2="1">
          <stop offset="0" stop-color="#e9eef3"/>
          <stop offset="0.5" stop-color="#c8d3de"/>
          <stop offset="1" stop-color="#9fb0c2"/>
        </linearGradient>
        <linearGradient id="writing-photo" x1="0" x2="1" y1="0" y2="1">
          <stop offset="0" stop-color="#e8eef4"/>
          <stop offset="0.6" stop-color="#c9d6e2"/>
          <stop offset="1" stop-color="#7fa3c8"/>
        </linearGradient>
      </defs>
      <rect x="0" y="317" width="1000" height="53" fill="url(#bar-gradient)"/>
      <polygon points="210,317 226,317 208,370 192,370" fill="#7a45a8" opacity="0.6"/>
      <polygon points="468,317 484,317 466,370 450,370" fill="#7a45a8" opacity="0.6"/>
      <path d="M668,0 L690,0 Q720,35 710,80 Q700,30 668,0 Z" fill="var(--sky)"/>
      <ellipse cx="842" cy="150" rx="262" ry="222" fill="var(--violet)"/>
      <ellipse cx="846" cy="146" rx="254" ry="214" fill="var(--white)"/>
      <ellipse cx="850" cy="145" rx="250" ry="208" fill="url(#desk-photo)" role="img" aria-label="Photo of a stethoscope resting on an ECG printout"/>
      <circle cx="510" cy="70" r="118" fill="var(--plum)"/>
      <circle cx="504" cy="70" r="114" fill="url(#writing-photo)" role="img" aria-label="Photo of a clinician's hands writing on a clipboard"/>
    </svg>

    <div class="headline-script">Medical billing</div>
    <div class="headline-bold">Tailored to your<br>practices needs</div>
    <div class="service-band">SERVICE</div>

    <ul class="service-list service-list--left">
      <li>Posting and Claim Processing</li>
      <li>Billing all Insurance Companies</li>
      <li>Claim Follow-up and Resubmission</li>
      <li>Remittance and payment posting</li>
    </ul>
    <ul class="service-list service-list--right">
      <li>Reconciliation of EOPs</li>
      <li>Insurance Appeal</li>
      <li>Insurance credentialing</li>
      <li>Billing audits</li>
    </ul>

    <div class="contact-row contact-phone">
      <svg width="16" height="16" viewBox="0 0 16 16" aria-hidden="true">
        <circle cx="8" cy="8" r="8" fill="#fff"/>
        <path d="M5.2 3.8 L6.6 5.6 L5.9 6.6 Q6.8 8.6 9.4 10.1 L10.4 9.4 L12.2 10.8 L11.2 12.3 Q7 12 3.8 5 Z" fill="#4a2d8f"/>
      </svg>(555) 014-2287
    </div>
    <div class="contact-row contact-email">Admin@velamedicalbilling.com</div>
    <div class="contact-row contact-web">velamedicalbilling.com</div>

    <div class="brand-name"><span class="brand-dot"></span>VELA<br>MEDICAL BILLING</div>
  </section>
</body>
</html>
```